Business Card Design (NEW FILES)

ATTENTION: New vector files are available. Please update your design to reflect/use the new (better resolution) logo images.

Seeking a unique and professional business card design for a commercial drone photography/videography business. The layout should feature
the logo (attached) and include the following information:
978-512-6037
www.skyvantmedia.com
ORD Certified Remote Pilot

```html
<!DOCTYPE html>
<html lang="en">
<head>
<meta charset="utf-8">
<title>Skyvant Media – Business Card</title>
<link href="https://fonts.googleapis.com/css2?family=Open+Sans:wght@400;600;700&display=swap" rel="stylesheet">
<style>
  :root {
    --stage: #232323;
    --card: #ffffff;
    --navy: #1c1f4a;
    --orange: #e98f4e;
    --ink: #1c1f4a;
  }
  * { box-sizing: border-box; margin: 0; padding: 0; }
  html, body { width: 1200px; height: 780px; overflow: hidden; }
  body {
    background: var(--stage);
    font-family: "Open Sans", Arial, sans-serif;
    display: flex;
    align-items: center;
    justify-content: center;
    gap: 32px;
  }
  .card {
    position: relative;
    width: 560px;
    height: 320px;
    background: var(--card);
    box-shadow: 0 10px 24px rgba(0,0,0,.45);
    overflow: hidden;
  }
  .brand {
    display: flex;
    align-items: center;
    gap: 12px;
    color: var(--navy);
    font-weight: 700;
    letter-spacing: 1px;
    text-transform: uppercase;
    white-space: nowrap;
  }
  .brand-dot {
    border-radius: 50%;
    background: var(--orange);
    flex: none;
  }
  /* front */
  .card-front { display: flex; align-items: center; justify-content: center; }
  .card-front .brand { font-size: 38px; }
  .card-front .brand-dot { width: 26px; height: 26px; }
  /* back */
  .card-back .brand { position: absolute; left: 36px; top: 44px; font-size: 24px; }
  .card-back .brand-dot { width: 18px; height: 18px; }
  .person {
    position: absolute;
    right: 52px;
    top: 40px;
    text-align: right;
  }
  .person-name { font-size: 28px; font-weight: 700; line-height: 1.1; }
  .person-name .first { color: var(--orange); }
  .person-name .last { color: var(--navy); }
  .person-role { font-size: 15px; color: var(--navy); }
  .accent-bar {
    position: absolute;
    right: 0;
    top: 38px;
    width: 30px;
    height: 62px;
    background: var(--orange);
  }
  .credentials {
    position: absolute;
    left: 36px;
    top: 170px;
    color: var(--ink);
    font-size: 15px;
    line-height: 1.35;
  }
  .contact {
    position: absolute;
    left: 36px;
    top: 222px;
    list-style: none;
    color: var(--ink);
    font-size: 15px;
    line-height: 1.55;
  }
  .contact li { display: flex; align-items: center; gap: 10px; }
  .contact svg { width: 15px; height: 15px; flex: none; fill: var(--orange); }
</style>
</head>
<body>
  <section class="card card-front">
    <div class="brand"><span class="brand-dot"></span>Skyvant Media</div>
  </section>

  <section class="card card-back">
    <div class="brand"><span class="brand-dot"></span>Skyvant Media</div>

    <div class="person">
      <p class="person-name"><span class="first">Mark</span> <span class="last">Doyle</span></p>
      <p class="person-role">Owner</p>
    </div>
    <div class="accent-bar"></div>

    <div class="credentials">
      <p>ORD Certified Remote Pilot</p>
      <p>Fully Insured</p>
    </div>

    <ul class="contact">
      <li>
        <svg viewBox="0 0 24 24" aria-hidden="true"><path d="M6.6 10.8a15.1 15.1 0 0 0 6.6 6.6l2.2-2.2a1 1 0 0 1 1-.25 11.4 11.4 0 0 0 3.6.57 1 1 0 0 1 1 1V20a1 1 0 0 1-1 1A17 17 0 0 1 3 4a1 1 0 0 1 1-1h3.5a1 1 0 0 1 1 1c0 1.25.2 2.45.57 3.57a1 1 0 0 1-.25 1z"/></svg>
        978-512-6037
      </li>
      <li>
        <svg viewBox="0 0 24 24" aria-hidden="true"><path d="M12 2a10 10 0 1 0 0 20 10 10 0 0 0 0-20zm6.9 6h-2.9a15.6 15.6 0 0 0-1.4-3.6A8 8 0 0 1 18.9 8zM12 4c.8 1.2 1.5 2.5 1.9 4h-3.8c.4-1.5 1.1-2.8 1.9-4zM4.3 14a8.2 8.2 0 0 1 0-4h3.4a16 16 0 0 0 0 4zm.8 2h2.9c.3 1.3.8 2.5 1.4 3.6A8 8 0 0 1 5.1 16zM8 8H5.1a8 8 0 0 1 4.3-3.6C8.8 5.5 8.3 6.7 8 8zm4 12c-.8-1.2-1.5-2.5-1.9-4h3.8c-.4 1.5-1.1 2.8-1.9 4zm2.3-6H9.7a14.6 14.6 0 0 1 0-4h4.6a14.6 14.6 0 0 1 0 4zm.3 5.6c.6-1.1 1.1-2.3 1.4-3.6h2.9a8 8 0 0 1-4.3 3.6zm1.7-5.6a16 16 0 0 0 0-4h3.4a8.2 8.2 0 0 1 0 4z"/></svg>
        www.skyvantmedia.com
      </li>
      <li>
        <svg viewBox="0 0 24 24" aria-hidden="true"><path d="M3 5h18a1 1 0 0 1 1 1v12a1 1 0 0 1-1 1H3a1 1 0 0 1-1-1V6a1 1 0 0 1 1-1zm1 2.3V17h16V7.3l-8 5.3z M5.2 7 12 11.5 18.8 7z"/></svg>
        info@skyvantmedia.com
      </li>
    </ul>
  </section>
</body>
</html>
```